Seafood restaurant menu

I am looking for a new menu design for my cajun seafood restaurant. I want something modern and simple. Our menu is very small so just one page front and back. Preferred, menu size is (4.25"x11"), I have attach some images, but we will have more to give.
Updates

Need to give designer more time

Target Market(s)

young to middle aged customers

Industry/Entity Type

Restaurant Food industry

Colors
EB3D1F
EC4F4E
F09395
F8D3D4
FCEDEE

Requirements
Must have
• creativity and interesting
Nice to have
• I would like to see a clean and simple menu, but with good color placement and photos of the dishes

```html
<!DOCTYPE html>
<html lang="en">
<head>
<meta charset="utf-8">
<title>Cajun Claw Kitchen – Menu</title>
<link href="https://fonts.googleapis.com/css2?family=Barlow:wght@500;600&family=Barlow+Condensed:wght@400&family=Kaushan+Script&display=swap" rel="stylesheet">
<style>
:root{
  --red:#eb3d1f;
  --coral:#ec4f4e;
  --rose:#f09395;
  --blush:#f8d3d4;
  --mist:#fcedee;
  --ink:#2b2b2b;
  --soft-ink:#555;
  --frame:#1c1c1c;
  --stage:#ececec;
}
*{box-sizing:border-box;margin:0;padding:0}
html,body{width:678px;height:1200px;overflow:hidden;background:var(--stage)}
.canvas{position:relative;width:678px;height:1200px}
.menu-page{position:absolute;top:192px;width:315px;height:816px;overflow:hidden;
  background:radial-gradient(ellipse 180px 260px at 20% 40%,var(--mist),transparent 70%),
             radial-gradient(ellipse 160px 220px at 90% 75%,var(--mist),transparent 70%),#fff;
  box-shadow:0 2px 8px rgba(0,0,0,.12);
  font-family:"Barlow",sans-serif;color:var(--ink)}
.menu-page--front{left:14px}
.menu-page--back{left:349px}
.stripe-band{position:absolute;left:0;width:100%;height:20px;
  background:repeating-linear-gradient(90deg,var(--red) 0 9px,var(--coral) 9px 18px)}
.stripe-band--top{top:0}
.stripe-band--bottom{bottom:0;height:22px}
.hero-dish{position:absolute;left:-6px;width:327px}
.hero-dish--top{top:19px;height:131px;border-radius:0 0 50% 50%/0 0 100% 100%;
  border-bottom:4px solid var(--frame);
  background:radial-gradient(circle at 40% 30%,#e0a23a,#b5541e 55%,#4a2310)}
.hero-dish--bottom{top:655px;height:140px;border-radius:50% 50% 0 0/100% 100% 0 0;
  border-top:4px solid var(--frame);
  background:radial-gradient(circle at 55% 60%,#d8441c,#a3240f 50%,#3a1a10)}
.brand{position:absolute;top:190px;left:0;width:100%;text-align:center}
.brand-mark{display:inline-block;width:40px;height:40px;border-radius:50%;background:var(--red);margin-bottom:6px}
.brand-name{font-family:"Kaushan Script",cursive;color:var(--red);font-size:30px;line-height:1.05}
.section-pill{position:absolute;height:28px;border:1.5px solid var(--red);border-radius:16px;
  font-family:"Kaushan Script",cursive;color:var(--red);font-size:17px;line-height:25px;padding-left:10px;background:#fff}
.dish-photo{position:absolute;width:73px;height:99px;border:2px solid var(--frame)}
.photo-wings{background:linear-gradient(150deg,#c86a2a,#8a3a16 60%,#e2b04a)}
.photo-basket{background:linear-gradient(160deg,#5a4436,#c89250 55%,#7b5a40)}
.photo-sides{background:linear-gradient(170deg,#2a2420,#b8402c 55%,#d9a44a)}
.photo-extras{background:linear-gradient(160deg,#e8e2da,#3b342f 55%,#d29a3a)}
.photo-boil{background:linear-gradient(160deg,#2d2d2d,#c1401e 55%,#eaa23a)}
.photo-crab{background:linear-gradient(170deg,#6a1e14,#d2472a 50%,#8c2a18)}
.photo-table{background:linear-gradient(160deg,#4a3a2e,#c8a36a 50%,#6a4a32)}
.photo-flavor{background:linear-gradient(160deg,#a32a16,#e06a2a 55%,#5a1a10)}
.menu-row{position:absolute;display:flex;align-items:baseline;font-size:10px;font-weight:600;white-space:nowrap}
.menu-row .leader{flex:1;border-bottom:1px solid var(--ink);margin:0 4px;transform:translateY(-2px)}
.menu-row .price{font-weight:500}
sup{font-size:6px}
.note{position:absolute;font-family:"Barlow Condensed",sans-serif;font-size:9px;color:var(--soft-ink);line-height:13px}
.label{position:absolute;font-size:10px;font-weight:600;white-space:nowrap}
</style>
</head>
<body>
<div class="canvas">

  <section class="menu-page menu-page--front">
    <div class="stripe-band stripe-band--top"></div>
    <div class="hero-dish hero-dish--top" role="img" aria-label="Pan of seafood rice with shrimp, mussels and lemon"></div>

    <div class="brand">
      <div class="brand-mark"></div>
      <div class="brand-name">Cajun Claw<br>Kitchen</div>
    </div>

    <div class="section-pill" style="left:17px;top:319px;width:110px">Appetizer</div>
    <div class="dish-photo photo-wings" style="left:220px;top:313px" role="img" aria-label="Wings with garlic noodles"></div>
    <div class="menu-row" style="left:17px;top:362px;width:198px"><span>8pc. Wings</span><span class="leader"></span><span class="price"><sup>$</sup>14/8pc.</span></div>
    <div class="note" style="left:17px;top:375px">(Honey Lemon Pepper/Buffalo/Claw Bomb)</div>
    <div class="menu-row" style="left:17px;top:396px;width:165px"><span>Garlic Noodles</span><span class="leader"></span><span class="price"><sup>$</sup>7</span></div>

    <div class="section-pill" style="left:118px;top:424px;width:173px">Fried Seafood Baskets</div>
    <div class="note" style="right:24px;top:459px;text-align:right">(All baskets served with a side, Sweet<br>Potato Fries or Hush Puppies +1)</div>
    <div class="dish-photo photo-basket" style="left:17px;top:451px" role="img" aria-label="Fried seafood basket with onion rings"></div>
    <div class="menu-row" style="left:113px;top:491px;width:178px"><span>Fried Oysters</span><span class="leader"></span><span class="price"><sup>$</sup>12</span></div>
    <div class="menu-row" style="left:113px;top:505px;width:178px"><span>Fried Shrimp</span><span class="leader"></span><span class="price"><sup>$</sup>3</span></div>
    <div class="menu-row" style="left:113px;top:518px;width:178px"><span>Fried Catfish</span><span class="leader"></span><span class="price"><sup>$</sup>12</span></div>
    <div class="menu-row" style="left:113px;top:531px;width:178px"><span>Fried Calamari</span><span class="leader"></span><span class="price"><sup>$</sup>12</span></div>
    <div class="menu-row" style="left:113px;top:545px;width:178px"><span>Soft Shell Crab *</span><span class="leader"></span><span class="price"><sup>$</sup>15</span></div>

    <div class="section-pill" style="left:17px;top:566px;width:110px">Sides</div>
    <div class="dish-photo photo-sides" style="left:220px;top:568px" role="img" aria-label="Loaded cajun fries"></div>
    <div class="menu-row" style="left:24px;top:610px;width:178px"><span>Cajun Fries</span><span class="leader"></span><span class="price"><sup>$</sup>5</span></div>
    <div class="menu-row" style="left:24px;top:624px;width:178px"><span>Sweet Potato Fries</span><span class="leader"></span><span class="price"><sup>$</sup>6</span></div>
    <div class="menu-row" style="left:24px;top:637px;width:178px"><span>Hush Puppies</span><span class="leader"></span><span class="price"><sup>$</sup>6</span></div>
    <div class="menu-row" style="left:24px;top:650px;width:178px"><span>Coleslaw</span><span class="leader"></span><span class="price"><sup>$</sup>4</span></div>
    <div class="menu-row" style="left:24px;top:664px;width:178px"><span>Steamed Rice</span><span class="leader"></span><span class="price"><sup>$</sup>3</span></div>

    <div class="dish-photo photo-extras" style="left:17px;top:683px;height:100px" role="img" aria-label="Boiled eggs, corn and potatoes"></div>
    <div class="section-pill" style="left:106px;top:685px;width:109px">Extras</div>
    <div class="menu-row" style="left:106px;top:724px;width:128px"><span>Potatoes (3pc)</span><span class="leader"></span><span class="price"><sup>$</sup>3</span></div>
    <div class="menu-row" style="left:106px;top:737px;width:128px"><span>Corn on the cob(2pc)</span><span class="leader"></span><span class="price"><sup>$</sup>3</span></div>
    <div class="menu-row" style="left:106px;top:750px;width:128px"><span>Boiled Eggs (2pc)</span><span class="leader"></span><span class="price"><sup>$</sup>3</span></div>
    <div class="menu-row" style="left:106px;top:764px;width:186px"><span>Sausage</span><span class="leader"></span><span class="price"><sup>$</sup>5 ½ LB / <sup>$</sup>9 1Lb</span></div>
    <div class="menu-row" style="left:106px;top:777px;width:151px"><span>Sauce</span><span class="leader"></span><span class="price"><sup>$</sup>6/Cup</span></div>

    <div class="stripe-band stripe-band--bottom"></div>
  </section>

  <section class="menu-page menu-page--back">
    <div class="stripe-band stripe-band--top"></div>

    <div class="section-pill" style="left:122px;top:34px;width:173px">Seafood by the LB</div>
    <div class="dish-photo photo-boil" style="left:21px;top:68px;height:98px" role="img" aria-label="Seafood boil tray with crab legs"></div>
    <div class="menu-row" style="left:104px;top:71px;width:160px"><span>Crawfish</span><span class="leader"></span><span class="price"><sup>$</sup>18</span></div>
    <div class="menu-row" style="left:104px;top:84px;width:160px"><span>Shrimp w/ head</span><span class="leader"></span><span class="price"><sup>$</sup>18</span></div>
    <div class="menu-row" style="left:104px;top:98px;width:160px"><span>Shrimp w/o head deveined</span><span class="leader"></span><span class="price"><sup>$</sup>20</span></div>
    <div class="menu-row" style="left:104px;top:111px;width:160px"><span>Clams</span><span class="leader"></span><span class="price"><sup>$</sup>18</span></div>
    <div class="menu-row" style="left:104px;top:125px;width:160px"><span>Mussels</span><span class="leader"></span><span class="price"><sup>$</sup>18</span></div>
    <div class="menu-row" style="left:104px;top:138px;width:160px"><span>Snow Crab legs</span><span class="leader"></span><span class="price"><sup>$</sup>39</span></div>
    <div class="menu-row" style="left:104px;top:151px;width:191px"><span>Lobster tail</span><span class="leader"></span><span class="price">Seasonal</span></div>
    <div class="menu-row" style="left:104px;top:165px;width:191px"><span>King Crab Legs</span><span class="leader"></span><span class="price">Seasonal</span></div>

    <div class="section-pill" style="left:21px;top:196px;width:120px">Seafood Plates</div>
    <div class="note" style="left:23px;top:230px">(All plates come with 1 flavor, 1 Corn, Sausages, and 1 Potato)</div>
    <div class="dish-photo photo-crab" style="left:223px;top:210px;height:100px" role="img" aria-label="Platter of snow crab clusters"></div>
    <div class="menu-row" style="left:23px;top:249px;width:176px"><span>Seafood plate 2 LB (1 flavor)</span><span class="leader"></span><span class="price"><sup>$</sup>38</span></div>
    <div class="note" style="left:23px;top:262px">2LB Choice of Shrimp/Clams/Mussel/Crawfish</div>
    <div class="menu-row" style="left:23px;top:279px;width:176px"><span>Snow Crab plate</span><span class="leader"></span><span class="price"><sup>$</sup>58</span></div>
    <div class="note" style="left:23px;top:292px;width:195px">1LB Snow Crab and 1LB Choice of Shrimp/Clams/<br>Mussel/Crawfish</div>

    <div class="section-pill" style="left:173px;top:337px;width:122px">Family Meals</div>
    <div class="dish-photo photo-table" style="left:21px;top:373px" role="img" aria-label="Family table with shared seafood plates"></div>
    <div class="menu-row" style="left:104px;top:377px;width:138px"><span>Seafood Combo 3 LB (1 flavor)</span><span class="leader"></span><span class="price"><sup>$</sup>60</span></div>
    <div class="note" style="left:104px;top:389px">Choice of Shrimp/Clams/Mussel/Crawfish, ½ LB Sausage,<br>2 Corns, 2 Potato, 2 Eggs, (2cups) Fountain Soda<br>(Substitute 1LB for Snow Crab + 20)</div>
    <div class="menu-row" style="left:104px;top:433px;width:180px"><span>Snow Crab Deluxe 4 LB (1 flavor)</span><span class="leader"></span><span class="price"><sup>$</sup>130</span></div>
    <div class="note" style="left:104px;top:445px">6 clusters of Snow Crab (3LB), 1LB choice of Shrimp/<br>Clams/Mussel/Crawfish, 1LB Sausage, 4 Corns, 4 Potato,<br>4 Eggs, (2cups) Fountain Soda</div>

    <div class="section-pill" style="left:21px;top:494px;width:141px">Choose your flavor</div>
    <div class="menu-row" style="left:23px;top:533px;width:106px"><span>Cajun (classic)</span><span class="leader"></span></div>
    <div class="label" style="left:134px;top:533px">Lemon Pepper</div>
    <div class="menu-row" style="left:23px;top:553px;width:106px"><span>Garlic Butter</span><span class="leader"></span></div>
    <div class="label" style="left:134px;top:553px">Claw Bomb</div>
    <div class="label" style="left:23px;top:574px">Spice it up:</div>
    <div class="note" style="left:23px;top:586px">Non-Spicy / Mild / Medium /Hot</div>
    <div class="label" style="left:23px;top:607px">Drinks:</div>
    <div class="note" style="left:23px;top:619px">Cola/Diet Cola/Zero Cola/Lemon-Lime</div>
    <div class="menu-row" style="left:23px;top:633px;width:168px"><span>20oz Fountain&nbsp;&nbsp;&nbsp;&nbsp;(Free Refill)</span><span class="leader"></span><span class="price"><sup>$</sup>3</span></div>
    <div class="dish-photo photo-flavor" style="left:223px;top:532px" role="img" aria-label="Seasoned crab legs with corn"></div>

    <div class="hero-dish hero-dish--bottom" role="img" aria-label="Crawfish, mussels and lemon on a wooden board"></div>
    <div class="stripe-band stripe-band--bottom"></div>
  </section>

</div>
</body>
</html>
```